I need a box design created for a DNA Fitness Test

I need a modern and sleek box design for a fitness test. The box needs to have our logo on it and should be clean and modern. The Box is 9 Inches Long 3 and 3/4 inches wide, and 2 inches tall. Company logo attached. The company name is cedar vitality.

Target Market(s)

Fitness

Industry/Entity Type

Fitness

Requirements
Must have
• Our logo

```html
<!DOCTYPE html>
<html lang="en">
<head>
<meta charset="utf-8">
<title>Cedar Vitality – DNA Fitness Test Box Dieline</title>
<link rel="stylesheet" href="https://fonts.googleapis.com/css2?family=Montserrat:wght@300;400;500;700;800;900&display=swap">
<style>
  :root {
    --teal: #2dbba4;
    --green: #8cc84b;
    --heading-green: #7cc252;
    --ink: #111111;
    --body-ink: #222222;
    --paper: #ffffff;
    --stage: #ececec;
    --photo-grey: #bcbdc0;
    --flap-grey: #d7d8da;
    --mark-blue: #2a8fd0;
    --decor-soft: rgba(110, 196, 110, 0.22);
  }
  * { box-sizing: border-box; margin: 0; padding: 0; }
  html, body {
    width: 670px; height: 1200px; overflow: hidden;
    background: var(--stage);
    font-family: "Montserrat", sans-serif;
    color: var(--body-ink);
  }
  .dieline {
    position: absolute; left: 13px; top: 171px;
    width: 643px; height: 858px;
    box-shadow: 0 6px 18px rgba(0,0,0,.12);
    border-radius: 0 0 14px 14px;
  }
  .panel { position: absolute; left: 0; width: 643px; overflow: hidden; }

  /* side panels */
  .side-panel {
    height: 143px;
    display: flex; flex-direction: column; align-items: center; justify-content: center;
    text-align: center; color: var(--ink);
  }
  .side-panel--top { top: 0; background: linear-gradient(90deg, var(--teal), var(--green)); }
  .side-panel--top .side-panel__content { transform: rotate(180deg); }
  .side-panel--bottom { top: 411px; background: linear-gradient(90deg, var(--green), var(--teal)); }
  .side-panel__title { font-size: 30px; line-height: 1; letter-spacing: .2px; }
  .side-panel__title .light { font-weight: 300; }
  .side-panel__title .bold { font-weight: 900; }
  .side-panel__text { margin-top: 12px; font-size: 7.6px; line-height: 1.55; font-weight: 400; }

  /* front panel */
  .front-panel { top: 143px; height: 268px; background: var(--paper); }
  .front-panel__decor { position: absolute; top: 0; height: 268px; width: 165px; }
  .front-panel__decor--left { left: 0; background: linear-gradient(90deg, var(--decor-soft), rgba(255,255,255,0)); }
  .front-panel__decor--right { right: 0; background: linear-gradient(270deg, var(--decor-soft), rgba(255,255,255,0)); }
  .brand {
    position: absolute; left: 0; right: 0; top: 48px;
    display: flex; flex-direction: column; align-items: center;
    color: var(--ink); font-weight: 800;
  }
  .brand__dot { width: 44px; height: 44px; border-radius: 50%; background: var(--mark-blue); margin-bottom: 20px; }
  .brand__name { font-size: 43px; line-height: 1; letter-spacing: 1px; }
  .brand__sub { font-size: 15px; letter-spacing: 9px; margin-top: 6px; padding-left: 9px; }

  /* back panel */
  .back-panel { top: 554px; height: 268px; background: var(--paper); }
  .back-panel__photo { position: absolute; left: 0; top: 0; width: 643px; height: 268px; }
  .back-panel__copy { position: absolute; left: 40px; top: 38px; width: 282px; }
  .back-panel__title { font-size: 24px; font-weight: 700; color: var(--heading-green); line-height: 1.1; }
  .back-panel__text { margin-top: 8px; font-size: 7.6px; line-height: 1.55; }
  .back-panel__list { margin: 9px 0 0 11px; font-size: 7.6px; line-height: 1.6; }
  .back-panel__closing { margin-top: 9px; font-size: 7.6px; }
  .photo-placement {
    position: absolute; left: 472px; top: 125px; width: 143px; height: 107px;
    border: 1.5px solid #ffffff;
    display: flex; align-items: center; justify-content: center; text-align: center;
    color: #ffffff; font-size: 13px; font-weight: 700; line-height: 1.3;
  }

  /* glue flap */
  .glue-flap { top: 822px; height: 36px; background: var(--flap-grey); border-radius: 0 0 14px 14px; }
</style>
</head>
<body>
<main class="dieline">

  <section class="panel side-panel side-panel--top">
    <div class="side-panel__content">
      <h2 class="side-panel__title"><span class="light">DNA</span> <span class="bold">Fitness Test</span></h2>
      <p class="side-panel__text">Lorem Ipsum is simply dummy text of the printing and typesetting industry. Lorem<br>Ipsum has been the industry's standard dummy text ever since the 1500s.</p>
    </div>
  </section>

  <section class="panel front-panel">
    <div class="front-panel__decor front-panel__decor--left" role="img" aria-label="Green DNA helix illustration"></div>
    <div class="brand">
      <span class="brand__dot"></span>
      <span class="brand__name">CEDAR</span>
      <span class="brand__sub">VITALITY</span>
    </div>
    <div class="front-panel__decor front-panel__decor--right" role="img" aria-label="Green DNA helix illustration"></div>
  </section>

  <section class="panel side-panel side-panel--bottom">
    <div class="side-panel__content">
      <h2 class="side-panel__title"><span class="light">DNA</span> <span class="bold">Fitness Test</span></h2>
      <p class="side-panel__text">Lorem Ipsum is simply dummy text of the printing and typesetting industry. Lorem<br>Ipsum has been the industry's standard dummy text ever since the 1500s.</p>
    </div>
  </section>

  <section class="panel back-panel">
    <svg class="back-panel__photo" viewBox="0 0 643 268" role="img" aria-label="Photo of a runner on an urban waterfront path">
      <path d="M440,0 L643,0 L643,268 L328,268 C328,200 360,160 410,130 C450,105 430,45 440,0 Z" fill="#bcbdc0"/>
    </svg>
    <div class="back-panel__copy">
      <h2 class="back-panel__title">DNA Fitness Test</h2>
      <p class="back-panel__text">Lorem ipsum dolor sit amet, consectetur adipiscing elit, sed do eiusmod tempor incididunt ut labore et dolore magna aliqua. Eleifend quam adipiscing vitae proin sagittis nisl rhoncus mattis rhoncus. Platea dictumst quisque sagittis purus.</p>
      <ul class="back-panel__list">
        <li>Cras condimentum elit eu leo commodo aliquet.</li>
        <li>Cras aliquet nisl vel lobortis viverra.</li>
        <li>Cras aliquam nisl in nunc scelerisque, sed rutrum odio viverra.</li>
        <li>Cras ultrices nulla interdum est cursus, a convallis enim finibus.</li>
        <li>Fusce eu risus gravida, interdum elit ut, pellentesque ante.</li>
      </ul>
      <p class="back-panel__closing">Lorem ipsum dolor sit amet, consectetur adipiscing elit.</p>
    </div>
    <div class="photo-placement">PHOTO<br>PLACEMENT</div>
  </section>

  <div class="panel glue-flap"></div>

</main>
</body>
</html>
```